Brochure & Business card design

Looking for a new business card design i want it to be modern and sharp looking i usually order plastic business cards, and i would like to make the colors like the logo teal/charcoal i will like to have our services on icons with words.... our services are
ROOFING GUTTERS PAINTING PRESSURE WASHING EXTERIOR DESIGN & ATTIC VENTILATION. I also want to add my credentials

Target Market(s)

Oregon local market

Industry/Entity Type

Residential Construction

Contact Information for Business Card

Business info, services, number, website

Font styles to use
Serif
Sans Serif

Colors
33b8a4
5c5c5c
ffffff

Requirements
Must have
• Tomas Relke
• Cell:
• Office:
• Email:
• Website:
• also i need our social media icons
• Services ROOFING GUTTERS PAINTING PRESSURE WASHING EXTERIOR DESIGN & ATTIC VENTILATION
• -icons for number, web, email, cell
• OR #384152
• Wa #KTRAPLD547Q3
Nice to have
• -Clean design Front & Back
• -Icons
• -shape House just like logo design
• -First Impression
Should not have
• Not Busy or lost of eye contact

```html
<!DOCTYPE html>
<html lang="en">
<head>
<meta charset="utf-8">
<title>Ridgeline Home Exteriors – Business Card</title>
<link rel="stylesheet" href="https://fonts.googleapis.com/css2?family=Open+Sans:wght@400;600&family=Roboto+Slab:wght@600&display=swap">
<style>
  :root {
    --teal: #1c9585;
    --teal-brand: #33b8a4;
    --charcoal: #5c5c5c;
    --ink: #3a3a3a;
    --white: #ffffff;
    --rule: #a9a9a9;
    --stage: #e6e6e6;
  }
  * { margin: 0; padding: 0; box-sizing: border-box; }
  html, body { width: 1200px; height: 802px; overflow: hidden; }
  body { background: var(--stage); position: relative; font-family: "Open Sans", sans-serif; }

  .card {
    position: absolute; top: 274px; width: 443px; height: 265px;
    box-shadow: 3px 4px 8px rgba(0,0,0,.3); overflow: hidden;
  }
  .card--front { left: 136px; background: var(--white); }
  .card--back { left: 624px; background: var(--charcoal); }

  /* front */
  .brand {
    position: absolute; left: 22px; top: 112px; width: 186px;
    text-align: center; font-family: "Roboto Slab", serif; font-weight: 600;
    font-size: 17px; line-height: 1.2; color: var(--teal);
  }
  .divider-v { position: absolute; left: 219px; top: 65px; width: 1px; height: 138px; background: #d6d6d6; }
  .person {
    position: absolute; left: 246px; top: 70px;
    font-family: "Roboto Slab", serif; font-weight: 600; font-size: 18px; color: var(--teal);
  }
  .person .surname { color: var(--charcoal); }
  .contact-list { position: absolute; left: 244px; top: 101px; list-style: none; color: var(--ink); font-size: 13px; }
  .contact-list li { display: flex; align-items: center; height: 16px; }
  .contact-list svg { width: 10px; height: 10px; margin-right: 6px; fill: var(--teal); flex: none; }
  .licences { position: absolute; left: 246px; top: 170px; font-size: 13px; line-height: 16px; color: var(--ink); }
  .footer-rule { position: absolute; left: 38px; top: 237px; width: 360px; height: 1px; background: var(--rule); }
  .social { position: absolute; left: 179px; top: 229px; display: flex; gap: 3px; padding: 0 4px; background: var(--white); }
  .social span { width: 16px; height: 16px; border-radius: 50%; background: #2b62a8; }

  /* back */
  .back-field { position: absolute; left: 0; top: 0; width: 100%; height: 201px; background: var(--teal); }
  .services {
    position: absolute; left: 88px; top: 90px; display: grid;
    grid-template-columns: 142px auto; row-gap: 4px;
    list-style: none; color: var(--white); font-size: 11.5px; text-transform: uppercase;
  }
  .services li { display: flex; align-items: center; height: 14px; }
  .services li::before { content: ""; width: 6px; height: 6px; border-radius: 50%; background: var(--white); margin-right: 3px; }
  .badge-frame { position: absolute; background: var(--teal); padding: 4px 4px 8px; }
  .badge-frame--roofing { left: 84px; top: 195px; width: 122px; height: 49px; }
  .badge-frame--accredited { left: 231px; top: 197px; width: 112px; height: 45px; }
  .badge { width: 100%; height: 100%; border-radius: 2px; }
  .badge--roofing { background: #f4f4f4; border-bottom: 5px solid #d9252a; }
  .badge--accredited { background: #111; border: 2px solid var(--white); }
</style>
</head>
<body>
  <section class="card card--front" aria-label="Business card front">
    <div class="brand">Ridgeline<br>Home Exteriors</div>
    <div class="divider-v"></div>
    <h1 class="person">TOMAS <span class="surname">RELKE</span></h1>
    <ul class="contact-list">
      <li><svg viewBox="0 0 10 10"><path d="M1 3.5C1 2 3 1.5 5 1.5S9 2 9 3.5L7.5 4 7 3H3L2.5 4ZM2.5 5h5l1 4h-7Z"/></svg>055-310 742 618</li>
      <li><svg viewBox="0 0 10 10"><path d="M3 0.5h4a1 1 0 0 1 1 1v7a1 1 0 0 1-1 1H3a1 1 0 0 1-1-1v-7a1 1 0 0 1 1-1Zm0.5 1.5v5.5h3V2Z"/></svg>055-310 742 618</li>
      <li><svg viewBox="0 0 10 10"><path d="M0.5 2h9v6h-9ZM1.5 3v.3L5 5.6l3.5-2.3V3L5 5.2Z"/></svg>info@ridgelinehx.com</li>
      <li><svg viewBox="0 0 10 10"><circle cx="5" cy="5" r="4.5"/></svg>www.ridgelinehx.com</li>
    </ul>
    <p class="licences">OR #384152<br>Wa #KTRAPLD547Q3</p>
    <div class="footer-rule"></div>
    <div class="social" aria-label="Social media links"><span></span><span></span><span></span><span></span></div>
  </section>

  <section class="card card--back" aria-label="Business card back">
    <div class="back-field"></div>
    <ul class="services">
      <li>Roofing</li><li>Gutters</li>
      <li>Painting</li><li>Pressure Washing</li>
      <li>Exterior Design</li><li>Attic Ventilation</li>
    </ul>
    <div class="badge-frame badge-frame--roofing"><div class="badge badge--roofing" role="img" aria-label="Roofing contractor certification badge"></div></div>
    <div class="badge-frame badge-frame--accredited"><div class="badge badge--accredited" role="img" aria-label="Accredited business badge"></div></div>
  </section>
</body>
</html>
```